Piste Ondaflux Winter Season (crossing course in the snow

Our company will diversify its activity. It will propose a crossing course to be carried out in the snow. We want the flyer to reflect the “far north” winter spirit.
This activity is unique in Switzerland. The flyer must catch the visual of the 80% tourist clientele and send them the desire to try
Target Market(s)
The clientele will be for all is all from 16 years
Industry/Entity Type
Tourisme d'hiver
Font styles to use
Sans Serif
Colors
Designer to choose colors to be used in the design.
Requirements
Must have
- The logo "Piste Ondaflux" and "Combe-d'Orvaz Région Pics-de-Saron" and the 4 partner logos on the back must appear but cannot be modified except for the size while keeping the proportions. All texts must be on the flyer but can be changed according to the designer's style. Photos can be adapted and we want an attractive design concept with creativity matching the description. The format of the flyer must respect the template of the 2 files
Nice to have
- The color palette reflects winter tones
Should not have
- We are not interested in receiving a copy of my 2 files with only a font change and 2 size

```html
<!DOCTYPE html>
<html lang="fr">
<head>
<meta charset="utf-8">
<title>Piste Ondaflux – Winter Season</title>
<link href="https://fonts.googleapis.com/css2?family=Montserrat:wght@400;500;600;700;800&family=Arimo:wght@400;700&display=swap" rel="stylesheet">
<style>
  :root{
    --green:#8cc63f;
    --dark:#3a3a3a;
    --ink:#1a1a1a;
    --grey:#9a9a9a;
    --mist:#e4e5e6;
    --white:#ffffff;
    --red:#c8202f;
    --stage:#ececec;
  }
  *{margin:0;padding:0;box-sizing:border-box}
  html,body{width:865px;height:1200px;overflow:hidden;background:var(--stage)}
  body{position:relative;font-family:"Montserrat",sans-serif;color:var(--ink)}

  .page{position:absolute;top:317px;width:400px;height:566px;overflow:hidden;box-shadow:0 4px 14px rgba(0,0,0,.18)}
  .front{left:20px;background:var(--white)}
  .back{left:445px;background:var(--mist);font-family:"Arimo",sans-serif}

  /* front */
  .url{position:absolute;top:18px;left:85px;font-size:9px;letter-spacing:.5px;color:var(--green)}
  .brand{position:absolute;top:62px;left:0;width:400px;display:flex;justify-content:center;align-items:center;gap:10px;font-size:40px;font-weight:700;color:var(--ink);letter-spacing:-.5px;line-height:1}
  .brand-dot{width:18px;height:18px;border-radius:50%;background:var(--green)}
  .tagline{position:absolute;top:134px;left:0;width:400px;text-align:center;font-size:10px;letter-spacing:3px;color:var(--grey)}
  .season{position:absolute;top:165px;left:72px;width:256px;height:33px;border:1.5px solid var(--green);text-align:center;font-size:24px;line-height:30px;font-weight:500;letter-spacing:.5px}
  .season .light{color:#a8a8a8}
  .region{position:absolute;top:214px;left:0;width:400px;display:flex;justify-content:center;align-items:center;gap:6px;font-size:9px;font-weight:700;color:var(--red);line-height:1.15}
  .region-mark{width:13px;height:13px;border-radius:50%;background:var(--red)}
  .scene{position:absolute;left:0;top:0}
  .band-text{position:absolute;top:534px;font-weight:500}
  .band-green{left:10px;font-size:17px;color:var(--white)}
  .band-dark{left:233px;font-size:10px;color:var(--green);top:541px}

  /* back */
  .photo-back{position:absolute;inset:0;background:linear-gradient(160deg,#d2d4d5 0%,#eceded 45%,#d8dadb 100%)}
  .headline{position:absolute;top:28px;left:15px;width:371px;height:25px;background:var(--dark);color:var(--white);font-size:16px;font-weight:700;line-height:25px;text-align:center;letter-spacing:.3px}
  .intro{position:absolute;top:71px;left:0;width:400px;text-align:center;font-size:9px}
  .subhead{position:absolute;top:109px;left:21px;width:359px;height:19px;border:1.5px solid var(--dark);text-align:center;font-size:13px;line-height:16px;letter-spacing:.2px}
  .desc{position:absolute;top:138px;left:18px;width:364px;text-align:center;font-size:9.5px;line-height:13px}
  .prices{position:absolute;top:207px;left:47px;width:307px;height:152px;border:1.5px solid var(--ink);font-family:"Montserrat",sans-serif}
  .prices h2{font-family:"Arimo",sans-serif;font-size:16px;text-align:center;margin-top:6px}
  .row{position:absolute;left:24px;width:260px;font-size:11px;display:flex;justify-content:space-between}
  .row span:last-child{width:60px}
  .note{position:absolute;left:0;width:100%;text-align:center;font-size:11px}
  .snack{position:absolute;top:385px;left:0;width:400px;text-align:center;font-size:17px;font-weight:700}
  .foot{position:absolute;top:436px;right:16px;font-size:5.5px;color:#555}
  .contact{position:absolute;top:451px;left:0;width:400px;height:24px;background:var(--dark);color:var(--white);font-size:10.5px;display:flex;align-items:center}
  .contact-label{background:var(--green);color:var(--ink);font-family:"Montserrat",sans-serif;font-weight:600;font-size:9px;height:24px;line-height:24px;padding:0 14px 0 8px;clip-path:polygon(0 0,100% 0,88% 100%,0 100%);margin-right:14px}
  .contact-item{display:flex;align-items:center;gap:5px;margin-right:16px}
  .partners-zone{position:absolute;top:475px;left:0;width:400px;height:91px;background:var(--white)}
  .partners-title{position:absolute;top:29px;left:15px;font-size:9.5px;font-weight:700}
  .partner-list{position:absolute;top:58px;left:15px;right:15px;display:flex;justify-content:space-between;list-style:none;font-size:9.5px;color:var(--ink)}
</style>
</head>
<body>

<section class="page front">
  <svg class="scene" width="400" height="566" viewBox="0 0 400 566">
    <defs>
      <linearGradient id="snowPhoto" x1="0" y1="0" x2="0" y2="1">
        <stop offset="0" stop-color="#6f7275"/>
        <stop offset=".45" stop-color="#8a8d90"/>
        <stop offset="1" stop-color="#e6e8ea"/>
      </linearGradient>
    </defs>
    <polygon points="0,330 100,246 160,272 290,208 330,232 400,202 400,566 0,566" fill="#d6d6d6"/>
    <polygon role="img" aria-label="Photo d'un pilote casqué sur un véhicule tout-terrain électrique dans la neige" points="0,348 100,262 150,288 290,224 330,250 400,218 400,566 0,566" fill="url(#snowPhoto)"/>
    <polygon points="0,530 400,530 400,566 0,566" fill="#3a3a3a"/>
    <polygon points="0,530 218,530 226,548 218,566 0,566" fill="#8cc63f"/>
  </svg>
  <div class="url">www.piste-ondaflux.ch</div>
  <div class="brand"><span>Piste Ondaflux</span><span class="brand-dot"></span></div>
  <div class="tagline">La montagne vue différemment</div>
  <div class="season">WINTER <span class="light">SEASON</span></div>
  <div class="region"><span class="region-mark"></span><span>COMBE-D'ORVAZ<br>Région Pics-de-Saron</span></div>
  <div class="band-text band-green">Sentations garanties</div>
  <div class="band-text band-dark">Ouveture le 20 décembre 2021</div>
</section>

<section class="page back">
  <div class="photo-back" role="img" aria-label="Photo estompée de véhicules tout-terrain électriques sur la neige"></div>
  <div class="headline">OUVERT TOUS LES JOURS* DÈS 11H00</div>
  <p class="intro">Piste Ondaflux vous propose une activité unique et inédite en Suisse.</p>
  <div class="subhead">UN CIRCUIT DE FRANCHISSEMENT SUR NEIGE.</div>
  <p class="desc">Avec nos Trakavel®, nommées araignées électriques, affrontez les éléments mis en place sur nos parcours pour devenir le pilote tout terrain que vous n'avez jamais imaginé être.</p>
  <div class="prices">
    <h2>Séance de 20mn :</h2>
    <div class="row" style="top:40px"><span>Indviduelle :</span><span>CHF 40.-</span></div>
    <div class="row" style="top:64px"><span>Famille (4 personnes) :</span><span>CHF140.-</span></div>
    <div class="note" style="top:100px">Sortie de groupe sur mesure dès 8 personnes</div>
    <div class="note" style="top:131px">Activité accessible PMR sur réservation</div>
  </div>
  <div class="snack">Snack - bar - ambiance</div>
  <div class="foot">(*) : sous réserve des conditions météorologiques</div>
  <div class="contact">
    <span class="contact-label">CONTACT :</span>
    <span class="contact-item">
      <svg width="11" height="9" viewBox="0 0 11 9"><rect x=".5" y=".5" width="10" height="8" fill="none" stroke="#8cc63f"/><path d="M.5 .5 5.5 5 10.5 .5" fill="none" stroke="#8cc63f"/></svg>
      info@piste-ondaflux.ch
    </span>
    <span class="contact-item">
      <svg width="10" height="10" viewBox="0 0 10 10"><path d="M2 1 4 3 3 4.5Q4.5 6.5 5.5 7L7 6 9 8 7.5 9.5Q3 9 .5 2.5Z" fill="none" stroke="#8cc63f"/></svg>
      +41 77 555 01 23
    </span>
  </div>
  <div class="partners-zone">
    <div class="partners-title">Nos partenaires :</div>
    <ul class="partner-list">
      <li>Banque Altavia</li>
      <li>Fiduciaire Morand S.A</li>
      <li>Caisse Alpine du Rhône</li>
      <li>Strada</li>
    </ul>
  </div>
</section>

</body>
</html>
```